Business Cards, artwork for t-shirts and embroidery, letterhead, and envelopes
Professional appearance
Professional
Derek J Foulton, III
President
742 Harrowgate Lane, Ste 5
West Berlin, New Jersey 08357
dfoulton@stonewiseworksgrp.example
stonewiseworksgrp.example
Upload artwork of LHVG, I can provide,
K&R Pewter, NQT logo
TAG LINE: Decorative Concrete Consultants
Concrete Polishing
Concrete Countertop Design
Epoxy Coatings
Decorative Engraving and Concrete Artwork
Association logo1
association 2
chamber of commerce logo
Place on front of card somewhere

```html
<!DOCTYPE html>
<html lang="en">
<head>
<meta charset="utf-8">
<title>Stonewise Works Group – Business Card</title>
<link href="https://fonts.googleapis.com/css2?family=Arimo:wght@400;700&display=swap" rel="stylesheet">
<style>
  :root {
    --page-bg: #e9e6e1;
    --card-bg: #ffffff;
    --brand-green: #1f7a45;
    --deep-green: #0f5a30;
    --accent-orange: #e07a1f;
    --gold: #d9a25c;
    --gold-light: #f0cf9c;
    --text-dark: #3a3a3a;
    --rule: #9a9a9a;
  }
  html, body {
    margin: 0;
    width: 1200px;
    height: 780px;
    overflow: hidden;
    background: var(--page-bg);
    font-family: "Arimo", Arial, sans-serif;
  }
  .card {
    position: absolute;
    left: 100px;
    top: 90px;
    width: 1000px;
    height: 600px;
    background: var(--card-bg);
    border-radius: 28px;
    overflow: hidden;
    box-shadow: 0 4px 14px rgba(0,0,0,0.15);
  }
  .card-wave {
    position: absolute;
    inset: 0;
    width: 1000px;
    height: 600px;
  }
  .brand {
    position: absolute;
    left: 60px;
    top: 215px;
    width: 400px;
    display: flex;
    align-items: center;
    gap: 18px;
  }
  .brand-mark {
    flex: none;
    width: 64px;
    height: 64px;
    border-radius: 50%;
    background: var(--brand-green);
  }
  .brand-name {
    color: var(--brand-green);
    font-weight: 700;
    font-size: 30px;
    line-height: 1.1;
    letter-spacing: 1px;
    text-transform: uppercase;
  }
  .contact {
    position: absolute;
    left: 480px;
    top: 60px;
  }
  .contact-name {
    margin: 0;
    color: var(--brand-green);
    font-weight: 700;
    font-size: 34px;
  }
  .contact-title {
    margin: 6px 0 0;
    color: var(--accent-orange);
    font-weight: 700;
    font-size: 20px;
  }
  .details {
    margin-top: 30px;
    padding-left: 22px;
    border-left: 2px solid var(--rule);
    color: var(--text-dark);
    font-size: 20px;
    line-height: 1.35;
  }
  .address { margin: 0 0 26px; }
  .lines { list-style: none; margin: 0; padding: 0; }
  .lines li {
    display: flex;
    align-items: center;
    gap: 12px;
    margin-bottom: 6px;
  }
  .icon { width: 20px; height: 20px; flex: none; fill: var(--text-dark); }
</style>
</head>
<body>
  <article class="card">
    <svg class="card-wave" viewBox="0 0 1000 600" aria-hidden="true">
      <defs>
        <linearGradient id="goldBand" x1="0" x2="1" y1="0" y2="0">
          <stop offset="0" stop-color="var(--gold)"/>
          <stop offset="0.5" stop-color="var(--gold-light)"/>
          <stop offset="1" stop-color="var(--gold)"/>
        </linearGradient>
        <linearGradient id="greenBand" x1="0" x2="1" y1="0" y2="0">
          <stop offset="0" stop-color="var(--deep-green)"/>
          <stop offset="0.5" stop-color="var(--brand-green)"/>
          <stop offset="1" stop-color="var(--deep-green)"/>
        </linearGradient>
      </defs>
      <path d="M0 455 C 250 540, 600 520, 1000 410 L1000 600 L0 600 Z" fill="url(#goldBand)"/>
      <path d="M0 485 C 250 560, 600 540, 1000 425 L1000 600 L0 600 Z" fill="url(#greenBand)"/>
    </svg>

    <div class="brand">
      <span class="brand-mark"></span>
      <span class="brand-name">Stonewise<br>Works Group</span>
    </div>

    <section class="contact">
      <h1 class="contact-name">Derek J Foulton, III</h1>
      <p class="contact-title">President</p>
      <div class="details">
        <p class="address">742 Harrowgate Lane, Ste 5<br>West Berlin, New Jersey 08357</p>
        <ul class="lines">
          <li><svg class="icon" viewBox="0 0 24 24"><path d="M6.6 10.8a15 15 0 0 0 6.6 6.6l2.2-2.2c.3-.3.7-.4 1-.2 1.1.4 2.3.6 3.6.6.6 0 1 .4 1 1V20c0 .6-.4 1-1 1A17 17 0 0 1 3 4c0-.6.4-1 1-1h3.5c.6 0 1 .4 1 1 0 1.3.2 2.5.6 3.6.1.3 0 .7-.2 1z"/></svg>(T)8550104417</li>
          <li><svg class="icon" viewBox="0 0 24 24"><path d="M6.6 10.8a15 15 0 0 0 6.6 6.6l2.2-2.2c.3-.3.7-.4 1-.2 1.1.4 2.3.6 3.6.6.6 0 1 .4 1 1V20c0 .6-.4 1-1 1A17 17 0 0 1 3 4c0-.6.4-1 1-1h3.5c.6 0 1 .4 1 1 0 1.3.2 2.5.6 3.6.1.3 0 .7-.2 1z"/></svg>8560193328</li>
          <li><svg class="icon" viewBox="0 0 24 24"><path d="M8 2h8a2 2 0 0 1 2 2v16a2 2 0 0 1-2 2H8a2 2 0 0 1-2-2V4a2 2 0 0 1 2-2zm0 3v13h8V5z"/></svg>8560274951</li>
          <li><svg class="icon" viewBox="0 0 24 24"><path d="M5 3h12v5h2a2 2 0 0 1 2 2v8h-4v3H7v-3H3v-8a2 2 0 0 1 2-2V3zm2 2v3h8V5zm2 10v4h6v-4z"/></svg>8560193329</li>
          <li><svg class="icon" viewBox="0 0 24 24"><path d="M12 2a10 10 0 1 0 5 18.7l-1-1.7A8 8 0 1 1 20 12v1a2 2 0 0 1-4 0V7h-2v1a5 5 0 1 0 .9 7.1A4 4 0 0 0 22 13v-1A10 10 0 0 0 12 2zm0 13a3 3 0 1 1 0-6 3 3 0 0 1 0 6z"/></svg>dfoulton@stonewiseworksgrp.example</li>
        </ul>
      </div>
    </section>
  </article>
</body>
</html>
```